Flyer-Design für Werbeflyer Teamentwicklung/Coaching als pdf
Zielgruppe
ich berate Personen, Teams und Organisationseinheiten, überwiegend im Profitbereich. (Internationale Konzerne). Mein Beratungsspektrum ist Führung, Prozessverbesserungen, Teamentwicklung
Aufgabenstellung
Der Text ist in Anlehnung an meine HP, Teamentwicklung und Coaching und es sollte eine übersichtliche, infomative 1-2 Seiten entstehen, die ich als erste Werbung/Kontaktaufnahme versenden kann. Die Seiten sollen klar einen Überblick über mein "Schaffen" geben, sollen aber auch schon etwas von meiner Arbeitsweise deutlich machen. (Ich begriefe schnell, formuliere klar und arbeite sehr zielorientiert - allerdings auch schnörkellos!) Diese Seiten sollten überwiegend als Anhang an eine Mail fungieren, im Ausnahmefall aber auch versendet werden.
Das Logo, die Farbe, etc. analog zu meiner HP - ich lass mich da aber auch gern beraten, falls sie andere Ideen haben

```html
<!DOCTYPE html>
<html lang="de">
<head>
<meta charset="utf-8">
<title>Teamentwicklung – Brigitte Moser</title>
<link rel="stylesheet" href="https://fonts.googleapis.com/css2?family=Open+Sans:wght@400;600&family=Tinos:wght@700&display=swap">
<style>
  :root {
    --band: #b8c8c3;
    --band-dark: #9aa6a4;
    --plum: #760a57;
    --heading: #687270;
    --text: #676b6b;
    --white: #ffffff;
    --sky: #58b8e6;
    --sea: #7fd6d6;
    --wood: #8b7a66;
  }
  * { margin: 0; padding: 0; box-sizing: border-box; }
  html, body { width: 1200px; height: 846px; overflow: hidden; background: var(--white); }
  body { font-family: "Open Sans", Arial, sans-serif; color: var(--text); }

  .flyer { position: relative; width: 1200px; height: 846px; overflow: hidden; background: var(--white); }

  .hero-photo {
    position: absolute; left: 0; top: 0; width: 337px; height: 846px;
    background: linear-gradient(180deg, var(--sky) 0%, #9fd9ef 22%, var(--sea) 34%, #a8a096 48%, var(--wood) 75%, #6f6254 100%);
  }

  .accent-bar { position: absolute; left: 1043px; top: 0; width: 109px; height: 227px; background: var(--plum); }

  .header-band { position: absolute; left: 0; top: 27px; width: 1200px; height: 115px; background: var(--band); }

  .brand-box {
    position: absolute; left: 45px; top: 27px; width: 122px; height: 115px;
    background: linear-gradient(90deg, var(--band-dark) 50%, var(--white) 50%);
    display: flex; align-items: center; justify-content: center;
  }
  .brand-name { font-size: 15px; font-weight: 600; color: var(--heading); background: var(--white); padding: 3px 6px; }

  .motto { position: absolute; left: 685px; top: 34px; width: 467px; height: 99px; }
  .motto svg { position: absolute; inset: 0; }
  .motto-text {
    position: absolute; font-family: "Tinos", "Times New Roman", serif; font-weight: 700;
    color: var(--white); font-size: 20.5px; line-height: 34px;
  }
  .motto-line1 { left: 30px; top: 14px; }
  .motto-line2 { left: 104px; top: 48px; }
  .quote-mark { position: absolute; font-family: "Tinos", serif; font-weight: 700; color: var(--white); font-size: 34px; }
  .quote-open { left: 9px; top: 4px; }
  .quote-close { left: 455px; top: 56px; }

  .title { position: absolute; left: 411px; top: 176px; font-size: 35px; font-weight: 600; color: var(--heading); letter-spacing: 0.3px; line-height: 44px; }
  .subtitle { position: absolute; left: 486px; top: 218px; font-size: 27px; font-weight: 600; color: var(--heading); line-height: 34px; letter-spacing: 0.3px; }
  .subtitle .surname { color: var(--plum); }

  .intro { position: absolute; left: 411px; top: 274px; width: 742px; font-size: 18.4px; line-height: 22px; }

  .section-label { position: absolute; left: 411px; top: 392px; font-size: 17.5px; font-weight: 600; color: var(--heading); }

  .benefits { position: absolute; left: 411px; top: 436px; width: 355px; list-style: none; }
  .benefits li { position: relative; padding-left: 26px; font-size: 18.4px; line-height: 22px; margin-bottom: 11px; }
  .benefits li::before { content: ""; position: absolute; left: 0; top: 6px; width: 11px; height: 11px; background: var(--plum); }

  .body-copy { position: absolute; left: 816px; top: 436px; width: 340px; font-size: 18.4px; line-height: 22px; }
</style>
</head>
<body>
<main class="flyer">
  <div class="hero-photo" role="img" aria-label="Foto: hölzerner Steg mit weißem Geländer, der aufs türkisfarbene Meer unter blauem Himmel hinausführt"></div>
  <div class="accent-bar"></div>
  <div class="header-band"></div>

  <div class="brand-box"><span class="brand-name">Brigitte Moser</span></div>

  <div class="motto">
    <svg width="467" height="99" viewBox="0 0 467 99" fill="none" stroke="#ffffff" stroke-width="4">
      <polyline points="60,2 2,2 2,97 60,97"/>
      <polyline points="407,2 465,2 465,97 407,97"/>
    </svg>
    <span class="quote-mark quote-open">“</span>
    <p class="motto-text motto-line1">Zu erkennen was geschieht,</p>
    <p class="motto-text motto-line2">ist der Beginn der Veränderung.</p>
    <span class="quote-mark quote-close">”</span>
  </div>

  <h1 class="title">TEAMENTWICKLUNG</h1>
  <p class="subtitle">BRIGITTE <span class="surname">MOSER</span></p>

  <p class="intro">Teams sind lebendige Gebilde, die um erfolgreich zu sein, sich immer wieder neu ausrichten und koordinieren müssen. Das tun sie in aller Regel ohne fremde Hilfe - aber ab und zu ist es hilfreich, Impulse oder Entwicklungsförderung von außen bekommen.</p>

  <h2 class="section-label">DAZU GEHÖREN</h2>

  <ul class="benefits">
    <li>Eine sorgfältige Analyse der Situation und Festlegung gewünschter Resultate</li>
    <li>Überzeugende und förderliche Methoden, die die Lösungskompetenzen der Menschen im Team unterstützen</li>
    <li>Klare Führung durch den Widerstreit von Teaminteressen zwischen Verändern, Bewahren, Harmonie und Konfliktbearbeitung, klarem Feedback und Eintracht im Team</li>
    <li>Tragfähigkeit der Ergebnisse</li>
  </ul>

  <p class="body-copy">Is quiant, sequo tempore peligenimus dollest isitiur aut provitat eos magnationsed qui dolore plaborunt as archita doluptatia deri audam essi optatur ratiist abor aut laut eatium faccuptae et aut ut es sequam recest qui nem re es seque parchit apictem quid et volorererro eniasperem inimporem quam, il iscipidit officidi omnis culpa sus secabo. Sed et arum illenis simus sus recerrum des ut aut il magni consent. perem inimporem quam, il iscipidit officidi omnis culpa sus secabo. Sed et arum illenis simus sus recerrum des ut aut il magni consent.</p>
</main>
</body>
</html>
```